Design for 3.31” x 84” vinyl banner for tradeshow

Hello, I am looking for a design that will be printed on a 33.31” x 84” vinyl banner for my company’s tradeshow booth.

-Design

My vision: I want to give you the full background, because I think it’ll help. We design insulation for electronic tools that go in high temperature oilwells. Interestingly, a lot of the electronic tools that go down these oil wells are also used in geothermal wells. However the electronics would melt in these high temperature geothermal wells if they were not insulated. A lot of companies that make tools for the oil market are trying to re-purpose their existing tools for the geothermal market…..and to do this, they would need our insulation.

So, our sign needs to conveys this message: Trying to enter the geothermal logging market? it's as simple as increasing the temp. rating for your existing tools

This sign will be placed at our company’s booth at an industry tradeshow. The sign needs to have a similar style to our existing signs. I’ve included images of our booth and all of our other signs. This sign doesn’t have to be identical in artistic style, but be fairly similar.

-Art Requirements:

At least 1 Image of RDP logo

I’ve included several different variations. Use your judgement to select the one that you think is most fitting.

Do not use the portion of the logo that says “40 years”. Feel free to crop that out if you would like.

At least 2 images of logging tools. You can select more than 2 if you think that’s necessary. Logging tools are the long metal tubes.

I’ve included several pictures of different logging tools. I would like to see at least 2 pictures of tools on the banner. Please include the image titled “Full, double centarlizer” It could look cool if this picture extended the full length of the banner (just a suggestion). I purchased these images off of picvault.For the second image of the tool, feel free to include whatever tool you think looks best.

-Colors and font: Like I mentioned above, I would like it to look close to the other signs we have at our booth. Please select colors and fonts that will fit with our other signs.

-Other thoughts/suggestions

When most people in our industry think of geothermal, the automatically associate it with extremely high temperatures. I’m open to seeing warmer colors (orange/red) that help convey this idea.

I’m also open to seeing pictures of geothermal power plants, I included an image of this titled “geothermal” that you may use if you like. This is not mandatory, just a suggestion.

-Text: the main text needs to be: “Trying to enter the Geothermal logging market? Ask us about increasing the temperature rating for your existing tools” No other text is required.

Printing/Art specifications:

I’ll be giving the design I receive off art-hive to a local banner printing shop. I’ve included their printing and art guidelines, please take a look at it and let me know if you have any questions. It’s pretty detailed so I hope it provides you with enough information. The design would have to follow the requirements in the two attached word documents.

Target Market(s)

oil and gas professionals

Industry/Entity Type

oil and gas/geothermal

Font styles to use
Other font styles liked:
• Fonts similar the font used on our other tradeshow signs (images attached)

Colors
F0912C
F2A743
F7CA91
FBE8D2
FDF5EE

Requirements
Must have
• -At least 1 Image of RDP logo, At least 2 images of logging tools (1 of these 2 pictures must be image titled "full double centralizer", he main text needs to be: “Trying to enter the Geothermal logging market? Ask us about increasing the temperature rating for your existing tools” , the design must follow the requirements in the printing and art guideline documents I attached.
Nice to have
• please select colors and fonts that will fit with our other signs.

```html
<!DOCTYPE html>
<html lang="en">
<head>
<meta charset="utf-8">
<title>Geothermal Logging Market Banner</title>
<link rel="stylesheet" href="https://fonts.googleapis.com/css2?family=Archivo+Black&family=Archivo:wght@600&display=swap">
<style>
  :root {
    --orange-deep: #F0912C;
    --orange: #F2A743;
    --peach: #F7CA91;
    --cream: #FBE8D2;
    --ivory: #FDF5EE;
    --ink: #111111;
    --steel-dark: #5f5f5f;
    --steel-light: #a7a7a7;
    --backdrop: #d9dad5;
    --banner-white: #ffffff;
  }
  html, body {
    margin: 0;
    padding: 0;
    width: 1200px;
    height: 1200px;
    overflow: hidden;
    background: var(--backdrop);
  }
  .banner {
    position: absolute;
    left: 380px;
    top: 40px;
    width: 440px;
    height: 1120px;
    background: var(--banner-white);
    overflow: hidden;
    box-shadow: 0 6px 20px rgba(0,0,0,0.18);
  }
  .banner-art {
    position: absolute;
    inset: 0;
  }
  .top-strip {
    position: absolute;
    left: 0; top: 0;
    width: 100%;
    height: 38px;
    background: var(--peach);
  }
  .headline {
    position: absolute;
    top: 66px;
    left: 0;
    width: 100%;
    text-align: center;
    font-family: "Archivo Black", "Arial Black", sans-serif;
    color: var(--ink);
    line-height: 1;
    margin: 0;
  }
  .headline .lead {
    display: block;
    font-family: "Archivo", Arial, sans-serif;
    font-weight: 600;
    font-size: 27px;
    letter-spacing: 0.5px;
  }
  .headline .key {
    display: block;
    font-size: 43px;
    margin-top: 4px;
  }
  .headline-rule {
    position: absolute;
    top: 228px;
    left: 26px;
    width: 388px;
    height: 2px;
    background: var(--orange-deep);
  }
  .subline {
    position: absolute;
    top: 238px;
    left: 0;
    width: 100%;
    text-align: center;
    font-family: "Archivo", Arial, sans-serif;
    font-weight: 600;
    font-size: 19px;
    line-height: 1.35;
    color: var(--ink);
    margin: 0;
  }
  .tool {
    position: absolute;
    border-radius: 6px;
    transform-origin: center;
  }
  .tool-centralizer {
    left: 170px;
    top: 300px;
    width: 34px;
    height: 650px;
    background: linear-gradient(90deg, var(--steel-dark), var(--steel-light) 50%, var(--steel-dark));
    transform: rotate(17deg);
  }
  .tool-rod {
    left: 282px;
    top: 330px;
    width: 8px;
    height: 620px;
    background: linear-gradient(90deg, var(--steel-dark), var(--steel-light));
    transform: rotate(13deg);
  }
  .brand {
    position: absolute;
    left: 60px;
    top: 990px;
    display: flex;
    align-items: center;
    gap: 14px;
  }
  .brand-square {
    width: 64px;
    height: 64px;
    background: var(--ink);
  }
  .brand-name {
    font-family: "Archivo Black", "Arial Black", sans-serif;
    font-size: 24px;
    line-height: 1.1;
    color: var(--ink);
  }
</style>
</head>
<body>
  <main class="banner">
    <svg class="banner-art" viewBox="0 0 440 1120" width="440" height="1120" aria-hidden="true">
      <defs>
        <linearGradient id="heatBand" x1="0" y1="0" x2="0" y2="1">
          <stop offset="0" stop-color="#F7CA91"/>
          <stop offset="0.6" stop-color="#FBE8D2"/>
          <stop offset="1" stop-color="#FDF5EE"/>
        </linearGradient>
      </defs>
      <polygon points="0,470 440,345 440,352 0,478" fill="#F7CA91"/>
      <polygon points="0,490 440,365 440,785 0,940" fill="url(#heatBand)"/>
      <polygon points="0,948 440,792 440,800 0,956" fill="#F7CA91"/>
    </svg>

    <div class="top-strip"></div>

    <h1 class="headline">
      <span class="lead">TRYING TO ENTER THE</span>
      <span class="key">GEOTHERMAL</span>
      <span class="key">LOGGING MARKET?</span>
    </h1>
    <div class="headline-rule"></div>
    <p class="subline">Ask us about increasing the temperature<br>rating for your existing tools.</p>

    <div class="tool tool-centralizer" role="img" aria-label="Photo of a full double centralizer logging tool"></div>
    <div class="tool tool-rod" role="img" aria-label="Photo of a slim logging tool with centralizers"></div>

    <div class="brand">
      <div class="brand-square"></div>
      <div class="brand-name">REDPOINT<br>DOWNHOLE, Inc.</div>
    </div>
  </main>
</body>
</html>
```